BLUE HAVEN (Business Card for Training Company)

Blue Haven is a training and consultancy company with a focus on executive protection and medical. I would like the card to be nice and sharp, not overdone and in black and red. I would also like it to highlight that it is "A Dravin Company"

I would like it to be simple and highlight a few things.

1. Name
2. Title
3. Phone Number
4. Email

I would also like www.dravinholdings.example/blue-haven to be on the card somewhere.

Target Market(s)

Security Companies

Industry/Entity Type

Security

Contact Information for Business Card

Blue Haven is a training and consultancy company with a focus on executive protection and medical. I would like the card to be nice and sharp, not overdone and in black and red. I would also like it to highlight that it is "A Dravin Company" I would like it to be simple and highlight a few things. 1. Name 2. Title 3. Phone Number 4. Email I would also like www.dravinholdings.example/blue-haven to be on the card somewhere.

Requirements
Must have
• A Dravin Company listed on the card and the website
Nice to have
• Highlight Medical Training, Consultancy & Executive Protection Courses

```html
<!DOCTYPE html>
<html lang="en">
<head>
<meta charset="utf-8">
<title>Blue Haven — Business Card</title>
<link href="https://fonts.googleapis.com/css2?family=Arimo:wght@400;700&family=Lato:wght@400&family=Michroma&display=swap" rel="stylesheet">
<style>
  :root {
    --backdrop: #b3b3b3;
    --card-black: #202020;
    --card-red: #650000;
    --ink-white: #ffffff;
    --rule: #9a9a9a;
    --accent-red: #8e1b1b;
  }
  * { margin: 0; padding: 0; box-sizing: border-box; }
  html, body { width: 1200px; height: 1200px; overflow: hidden; }
  body { background: var(--backdrop); position: relative; }

  .card { position: absolute; top: 303px; height: 594px; color: var(--ink-white); }
  .card--front { left: 200px; width: 370px; background: var(--card-black); }
  .card--back { left: 599px; width: 365px; background: var(--card-red); }

  .wordmark {
    position: absolute;
    font-family: "Arimo", Arial, sans-serif;
    font-weight: 700;
    font-size: 60px;
    line-height: 54px;
    letter-spacing: 1px;
    color: var(--ink-white);
  }
  .card--front .wordmark { left: 70px; top: 142px; }
  .card--back .wordmark { left: 69px; top: 130px; }

  .parent-line {
    position: absolute; left: 0; width: 100%; top: 381px;
    text-align: center;
    font-family: "Arimo", Arial, sans-serif; font-size: 17px;
  }
  .parent-mark {
    position: absolute; top: 411px; left: 0; width: 100%;
    display: flex; justify-content: center; align-items: center; gap: 10px;
  }
  .parent-mark__square { width: 26px; height: 26px; background: var(--accent-red); }
  .parent-mark__name {
    font-family: "Arimo", Arial, sans-serif; font-weight: 700; font-size: 22px; letter-spacing: 1px;
  }
  .divider {
    position: absolute; top: 472px; left: 124px; width: 120px; height: 1px; background: var(--rule);
  }
  .services {
    position: absolute; top: 495px; left: 0; width: 100%;
    text-align: center; list-style: none;
    font-family: "Arimo", Arial, sans-serif; font-size: 17px; line-height: 21.5px;
  }

  .person {
    position: absolute; left: 0; width: 100%; top: 383px; text-align: center;
  }
  .person__name { font-family: "Michroma", sans-serif; font-size: 21px; font-weight: 400; letter-spacing: 0.5px; -webkit-text-stroke: 0.8px var(--ink-white); }
  .person__title { font-family: "Lato", sans-serif; font-size: 17px; margin-top: 4px; }

  .contact-icons {
    position: absolute; top: 456px; left: 0; width: 100%;
    display: flex; justify-content: center; align-items: center; gap: 4px;
  }
  .contact-icons__rule { width: 52px; height: 1px; background: var(--rule); margin: 0 4px; }
  .contact-icons__box {
    width: 25px; height: 25px; background: var(--ink-white); border-radius: 3px;
    display: flex; align-items: center; justify-content: center;
  }
  .contacts {
    position: absolute; top: 494px; left: 0; width: 100%;
    text-align: center; list-style: none;
    font-family: "Lato", sans-serif; font-size: 17px; line-height: 21.7px;
  }
  .contacts__web { font-size: 14px; }
</style>
</head>
<body>
  <section class="card card--front">
    <div class="wordmark">BLUE<br>HAVEN</div>
    <p class="parent-line">A DRAVIN COMPANY</p>
    <div class="parent-mark">
      <span class="parent-mark__square"></span>
      <span class="parent-mark__name">DRAVIN</span>
    </div>
    <div class="divider"></div>
    <ul class="services">
      <li>Medical Training</li>
      <li>Consultancy</li>
      <li>Executive Protection Courses</li>
    </ul>
  </section>

  <section class="card card--back">
    <div class="wordmark">BLUE<br>HAVEN</div>
    <div class="person">
      <h1 class="person__name">MARCUS HALE</h1>
      <p class="person__title">Managing Director</p>
    </div>
    <div class="contact-icons">
      <span class="contact-icons__rule"></span>
      <span class="contact-icons__box">
        <svg width="17" height="17" viewBox="0 0 24 24" aria-label="Phone"><path d="M3 9c0-3 18-3 18 0v2h-5V9H8v2H3z M6 12h12l2 8H4z" fill="#650000"/></svg>
      </span>
      <span class="contact-icons__box">
        <svg width="17" height="17" viewBox="0 0 24 24" aria-label="Email"><rect x="3" y="6" width="18" height="12" fill="none" stroke="#650000" stroke-width="2"/><path d="M3 6l9 7 9-7" fill="none" stroke="#650000" stroke-width="2"/></svg>
      </span>
      <span class="contact-icons__box">
        <svg width="17" height="17" viewBox="0 0 24 24" aria-label="Website"><circle cx="12" cy="12" r="9" fill="#650000"/><path d="M7 8c2 0 3 2 5 2s1 3-1 3-2 3-3 4M15 14c1 0 3 1 2 3" fill="none" stroke="#fff" stroke-width="1.8"/></svg>
      </span>
      <span class="contact-icons__rule"></span>
    </div>
    <ul class="contacts">
      <li>044-987 654 321</li>
      <li>info@bluehaven.example</li>
      <li class="contacts__web">www.dravinholdings.example/blue-haven</li>
    </ul>
  </section>
</body>
</html>
```